Business Card Design

I need a business card design for my law office based in Pasadena, California. I am a sole practitioner and I specialize in business transaction and litigation, probate and estate planning, taxation law, corporate and business formation, immigration and real estate. I want something that is simple, yet stands out.

A friend helped to create a logo about 6 years ago. I am open to new ideas to changing the logo.

Industry/Entity Type

Business

Contact Information for Business Card

Law Offices of Dorvan L. Mabry
842 W. Larkspur Ave., Suite 319
Pasadena, CA 90287
Tel: 626-555-0174
Fax: 626-555-0139
Email: dmabry@dlmlegalgroup.example

Attorney: Dorvan L. Mabry

```html
<!DOCTYPE html>
<html lang="en">
<head>
<meta charset="utf-8">
<title>Dorvan L. Mabry — Business Card</title>
<link href="https://fonts.googleapis.com/css2?family=Open+Sans:wght@400;600&display=swap" rel="stylesheet">
<style>
  :root {
    --olive: #a7a31c;
    --olive-dark: #77740f;
    --olive-light: #cfca45;
    --paper: #ffffff;
    --paper-shade: #eeeeee;
    --ink: #4a4a4a;
    --backdrop: #e4e2dc;
  }
  * { margin: 0; padding: 0; box-sizing: border-box; }
  html, body {
    width: 1200px; height: 1062px; overflow: hidden;
    background: var(--backdrop);
    font-family: "Open Sans", sans-serif;
  }
  .stage {
    width: 1200px; height: 1062px;
    display: flex; flex-direction: column; align-items: center; justify-content: center;
    gap: 56px;
  }
  .card {
    width: 770px; height: 440px; position: relative; overflow: hidden;
    box-shadow: 0 10px 26px rgba(0,0,0,.22);
  }
  /* Front */
  .card-front {
    background: linear-gradient(160deg, var(--paper) 40%, var(--paper-shade) 100%);
  }
  .front-band {
    position: absolute; left: 0; right: 0; bottom: 0; height: 112px;
    background: linear-gradient(100deg, var(--olive-dark) 0%, var(--olive) 45%, var(--olive-light) 100%);
  }
  .brand-block {
    position: absolute; left: 60px; top: 120px; width: 280px;
    display: flex; align-items: center; gap: 14px;
  }
  .brand-dot {
    width: 16px; height: 16px; border-radius: 50%; background: var(--olive); flex: none;
  }
  .brand-name {
    color: var(--olive); font-weight: 400; font-size: 22px; line-height: 1.3;
    letter-spacing: .5px;
  }
  .divider {
    position: absolute; left: 370px; top: 80px; width: 1px; height: 200px;
    background: linear-gradient(to bottom, transparent, var(--olive), transparent);
  }
  .contact {
    position: absolute; left: 410px; top: 70px; color: var(--ink);
  }
  .person-name { color: var(--olive); font-weight: 600; font-size: 20px; line-height: 1.2; }
  .person-title { font-size: 15px; margin-bottom: 18px; }
  .address { font-size: 15px; line-height: 1.5; margin-bottom: 12px; }
  .contact-line { display: flex; align-items: center; gap: 10px; font-size: 15px; line-height: 1.65; }
  .contact-line svg { width: 14px; height: 14px; fill: var(--olive); flex: none; }
  .contact-line .at { color: var(--olive); font-weight: 600; width: 14px; text-align: center; }
  /* Back */
  .card-back {
    background: radial-gradient(ellipse at 60% 45%, var(--olive-light) 0%, var(--olive) 45%, var(--olive-dark) 100%);
  }
  .back-brand {
    position: absolute; right: 60px; bottom: 60px;
    display: flex; align-items: center; gap: 14px;
  }
  .back-brand .brand-name { color: var(--paper); font-size: 24px; }
  .back-brand .brand-dot { background: var(--paper); }
</style>
</head>
<body>
<main class="stage">
  <section class="card card-front" aria-label="Card front">
    <div class="brand-block">
      <span class="brand-dot"></span>
      <span class="brand-name">Law Offices of<br>Dorvan L. Mabry</span>
    </div>
    <div class="divider"></div>
    <div class="contact">
      <p class="person-name">Dorvan L. Mabry</p>
      <p class="person-title">Lawyer</p>
      <p class="address">842 W. Larkspur Ave., Suite 319<br>Pasadena, CA 90287</p>
      <p class="contact-line">
        <svg viewBox="0 0 24 24" aria-hidden="true"><path d="M6.6 10.8a15.1 15.1 0 0 0 6.6 6.6l2.2-2.2a1 1 0 0 1 1-.25 11.4 11.4 0 0 0 3.6.57 1 1 0 0 1 1 1V20a1 1 0 0 1-1 1A17 17 0 0 1 3 4a1 1 0 0 1 1-1h3.5a1 1 0 0 1 1 1c0 1.25.2 2.45.57 3.57a1 1 0 0 1-.25 1z"/></svg>
        626-555-0174
      </p>
      <p class="contact-line">
        <svg viewBox="0 0 24 24" aria-hidden="true"><path d="M7 3h10v5H7zM4 9h16a2 2 0 0 1 2 2v6h-4v4H6v-4H2v-6a2 2 0 0 1 2-2zm4 7v3h8v-3z"/></svg>
        626-555-0139
      </p>
      <p class="contact-line"><span class="at">@</span> dmabry@dlmlegalgroup.example</p>
    </div>
    <div class="front-band"></div>
  </section>

  <section class="card card-back" aria-label="Card back">
    <div class="back-brand">
      <span class="brand-dot"></span>
      <span class="brand-name">Law Offices of Dorvan L. Mabry</span>
    </div>
  </section>
</main>
</body>
</html>
```